Bag / Pouch Retail Packaging Design.

Our Product (VELIRA Wall Bracket) Image attached with measurements.
We require a Pouch / Bag packaging design like the two examples attached.
- We have attached different file formats and colours of our logo.
- The internal area needs to fit our product - Measurements in the attached image.
- Flat Top and Bottom.
- Text to include on packaging:
www.bracklow.co.uk
Designed in the UK
Help: sales@bracklow.co.uk
We like the idea of a repeat pattern of our logo. But this is not a must, just an idea. (Example attached)
IMPORTANT: The packaging should only consist of two different colors. Colour options: Black, White, Grey or Green (Like the attached Image)
We DO NOT require an image of the product on the packaging.
On the back of the pouch, there needs to be a transparent window to see inside. Roughly 1/3 of the back total size.
Any questions please feel free to ask.
Look and feel
Each slider illustrates characteristics of the customer's brand and the style your logo design should communicate.

```html
<!DOCTYPE html>
<html lang="en">
<head>
<meta charset="utf-8">
<title>BRACKLOW Pouch Packaging – Front and Back</title>
<link rel="stylesheet" href="https://fonts.googleapis.com/css2?family=Montserrat:wght@400;600;700&display=swap">
<style>
  :root {
    --stage: #6b6b6b;
    --paper: #ffffff;
    --pattern-light: #fbfbfb;
    --pattern-mid: #e6e6e6;
    --ink: #060606;
    --ink-mid: #7a7a7a;
    --green: #14ae92;
    --green-ink: #1d3a34;
    --label: #2a2a2a;
    --check-a: #ffffff;
    --check-b: #cdcdcd;
  }
  * { box-sizing: border-box; margin: 0; padding: 0; }
  html, body {
    width: 1200px;
    height: 1200px;
    overflow: hidden;
    background: var(--stage);
    font-family: "Montserrat", sans-serif;
  }
  .sheet { position: relative; width: 1200px; height: 1200px; }
  .view { position: absolute; top: 235px; width: 400px; }
  .view--front { left: 160px; }
  .view--back { left: 640px; }
  .view__label {
    text-align: center;
    font-weight: 400;
    font-size: 42px;
    color: var(--label);
    margin-bottom: 48px;
    letter-spacing: 0.5px;
  }
  .panel {
    position: relative;
    width: 400px;
    height: 585px;
    background: var(--paper);
    overflow: hidden;
  }
  .panel__pattern {
    position: absolute;
    inset: 0;
    background: linear-gradient(160deg, var(--pattern-light), var(--pattern-mid));
  }
  .panel__brand {
    position: absolute;
    top: 62px;
    left: 0;
    right: 0;
    text-align: center;
    font-weight: 600;
    font-size: 44px;
    letter-spacing: 3px;
    color: var(--ink);
  }
  .panel__mark { position: absolute; }
  .view--front .panel__mark {
    left: 0;
    right: 0;
    top: 190px;
    bottom: 0;
    background: linear-gradient(90deg, var(--ink) 0%, var(--ink-mid) 35%, var(--pattern-mid) 50%, var(--ink-mid) 65%, var(--ink) 100%);
  }
  .view--back .panel__mark {
    left: 0;
    right: 0;
    top: 0;
    height: 400px;
    background: linear-gradient(90deg, var(--ink) 0%, var(--ink-mid) 35%, var(--pattern-mid) 50%, var(--ink-mid) 65%, var(--ink) 100%);
  }
  .panel__window {
    position: absolute;
    left: 0;
    top: 128px;
    width: 336px;
    height: 272px;
    background-color: var(--check-a);
    background-image: conic-gradient(var(--check-b) 25%, var(--check-a) 0 50%, var(--check-b) 0 75%, var(--check-a) 0);
    background-size: 34px 34px;
    opacity: 0.85;
  }
  .panel__info {
    position: absolute;
    left: 0;
    right: 0;
    bottom: 0;
    height: 99px;
    background: var(--green);
    color: var(--green-ink);
    text-align: center;
    font-weight: 600;
    font-size: 15.5px;
    line-height: 21px;
    padding-top: 18px;
  }
</style>
</head>
<body>
<main class="sheet">
  <section class="view view--front">
    <h2 class="view__label">Front</h2>
    <div class="panel">
      <div class="panel__pattern" role="img" aria-label="Faint grey repeat pattern of the brand mark"></div>
      <div class="panel__mark" role="img" aria-label="Large black brand mark decoration"></div>
      <p class="panel__brand">BRACKLOW</p>
    </div>
  </section>

  <section class="view view--back">
    <h2 class="view__label">Back</h2>
    <div class="panel">
      <div class="panel__pattern" role="img" aria-label="Faint grey repeat pattern of the brand mark"></div>
      <div class="panel__mark" role="img" aria-label="Large black brand mark decoration"></div>
      <div class="panel__window" role="img" aria-label="Transparent window showing the product inside"></div>
      <div class="panel__info">
        <p>Designed in the UK</p>
        <p>www.bracklow.co.uk</p>
        <p>Help: sales@bracklow.co.uk</p>
      </div>
    </div>
  </section>
</main>
</body>
</html>
```